real esate business card with company logo and name

we need a business card design for a real esate company

The company name is Walsh & Brody Pty Ltd, and we have our logo designed and will upload. We want classic or moden feel. Black or white background. looks more textured. Should include folowinginformations
Paul Walsh and Lucy Brody
Sales Agents & Onsite Manager
p: 07 5948 2063
F: 07 5948 2174
M:0461 857 239
3/42 Marlin Crescent, ELLEN GROVE QLD 4078

We want this business card looks professonal. Thank you in advance.

Industry/Entity Type

Real Estate Agent

Contact Information for Business Card

Paul Walsh and Lucy Brody
Onsite Manager & Sales Agents
p: 07 5948 2063
M:0461 857 239

Font styles to use
Serif

Colors
000000
fbfbfb
333333
959595

Requirements
Must have
• company logo and name, black or white back ground

```html
<!DOCTYPE html>
<html lang="en">
<head>
<meta charset="utf-8">
<title>Walsh &amp; Brody Pty Ltd — Business Cards</title>
<link href="https://fonts.googleapis.com/css2?family=Questrial&family=Arimo:wght@400&display=swap" rel="stylesheet">
<style>
  :root {
    --ink: #000000;
    --paper: #fbfbfb;
    --dark: #333333;
    --grey: #959595;
    --stage: #e6e6e6;
    --texture-a: #ffffff;
    --texture-b: #efefef;
  }
  * { margin: 0; padding: 0; box-sizing: border-box; }
  html, body { width: 1200px; height: 900px; overflow: hidden; }
  body { background: var(--stage); position: relative; }

  .card {
    position: absolute;
    width: 660px;
    height: 400px;
    background: var(--paper);
    box-shadow: 0 2px 10px rgba(0,0,0,0.12);
    overflow: hidden;
  }
  .card--paul { left: 60px; top: 40px; }
  .card--lucy { left: 480px; top: 460px; }

  .card__texture {
    position: absolute;
    inset: 0;
    background: linear-gradient(200deg, var(--texture-a) 0%, var(--texture-a) 40%, var(--texture-b) 100%);
  }

  .brand {
    position: absolute;
    left: 40px;
    top: 110px;
    width: 270px;
    display: flex;
    flex-direction: column;
    align-items: center;
    gap: 22px;
  }
  .brand__square {
    width: 130px;
    height: 130px;
    background: var(--grey);
  }
  .brand__name {
    font-family: "Questrial", sans-serif;
    font-size: 17px;
    letter-spacing: 1px;
    color: var(--dark);
    white-space: nowrap;
  }

  .details {
    position: absolute;
    left: 330px;
    top: 62px;
    color: var(--ink);
  }
  .details__name {
    font-family: "Questrial", sans-serif;
    font-size: 28px;
    letter-spacing: 2px;
    line-height: 1;
  }
  .details__role {
    font-family: "Arimo", sans-serif;
    font-size: 18px;
    color: var(--dark);
    margin-top: 8px;
  }
  .contact {
    list-style: none;
    margin-top: 26px;
    font-family: "Arimo", sans-serif;
    font-size: 21px;
    line-height: 27px;
  }
  .contact__item { display: flex; align-items: center; gap: 10px; }
  .contact__icon { width: 18px; height: 18px; flex: none; fill: var(--dark); }
  .address {
    margin-top: 24px;
    font-family: "Arimo", sans-serif;
    font-style: normal;
    font-size: 21px;
    line-height: 27px;
  }
</style>
</head>
<body>

<article class="card card--paul">
  <div class="card__texture" role="img" aria-label="Faint repeated pattern texture across the card"></div>
  <div class="brand">
    <div class="brand__square"></div>
    <div class="brand__name">WALSH &amp; BRODY PTY LTD.</div>
  </div>
  <div class="details">
    <h1 class="details__name">PAUL WALSH</h1>
    <p class="details__role">Sales Agents &amp; Onsite Manager</p>
    <ul class="contact">
      <li class="contact__item">
        <svg class="contact__icon" viewBox="0 0 18 18" aria-label="Phone"><path d="M4 2c1 0 2 2 2.5 3.5L5 7c1 2.5 3.5 5 6 6l1.5-1.5C14 12 16 13 16 14c0 1.5-1.5 2.5-3 2.5C7 16.5 1.5 11 1.5 5 1.5 3.5 2.5 2 4 2z"/></svg>
        07 5948 2063
      </li>
      <li class="contact__item">
        <svg class="contact__icon" viewBox="0 0 18 18" aria-label="Fax"><rect x="4" y="1" width="10" height="6"/><rect x="1" y="7" width="16" height="7" rx="1"/><rect x="4" y="12" width="10" height="5" fill="#fbfbfb" stroke="#333" stroke-width="1.5"/></svg>
        07 5948 2174
      </li>
      <li class="contact__item">
        <svg class="contact__icon" viewBox="0 0 18 18" aria-label="Mobile"><rect x="4" y="1" width="10" height="16" rx="1.5"/><rect x="6" y="3" width="6" height="5" fill="#fbfbfb"/></svg>
        0461 857 239
      </li>
    </ul>
    <address class="address">3/42 Marlin Crescent,<br>ASHWOOD VALE QLD 4215</address>
  </div>
</article>

<article class="card card--lucy">
  <div class="card__texture" role="img" aria-label="Faint repeated pattern texture across the card"></div>
  <div class="brand">
    <div class="brand__square"></div>
    <div class="brand__name">WALSH &amp; BRODY PTY LTD.</div>
  </div>
  <div class="details">
    <h1 class="details__name">LUCY BRODY</h1>
    <p class="details__role">Sales Agents &amp; Onsite Manager</p>
    <ul class="contact">
      <li class="contact__item">
        <svg class="contact__icon" viewBox="0 0 18 18" aria-label="Phone"><path d="M4 2c1 0 2 2 2.5 3.5L5 7c1 2.5 3.5 5 6 6l1.5-1.5C14 12 16 13 16 14c0 1.5-1.5 2.5-3 2.5C7 16.5 1.5 11 1.5 5 1.5 3.5 2.5 2 4 2z"/></svg>
        07 5948 2063
      </li>
      <li class="contact__item">
        <svg class="contact__icon" viewBox="0 0 18 18" aria-label="Fax"><rect x="4" y="1" width="10" height="6"/><rect x="1" y="7" width="16" height="7" rx="1"/><rect x="4" y="12" width="10" height="5" fill="#fbfbfb" stroke="#333" stroke-width="1.5"/></svg>
        07 5948 2174
      </li>
      <li class="contact__item">
        <svg class="contact__icon" viewBox="0 0 18 18" aria-label="Mobile"><rect x="4" y="1" width="10" height="16" rx="1.5"/><rect x="6" y="3" width="6" height="5" fill="#fbfbfb"/></svg>
        0461 857 239
      </li>
    </ul>
    <address class="address">3/42 Marlin Crescent,<br>ASHWOOD VALE QLD 4215</address>
  </div>
</article>

</body>
</html>
```